Bramble Peak Information Technology Business Card
Services for Move Add Change, Technical Relocation, Server Room Support, Technical Support
Bramble Peak Information Technology Business Card - Information Technology
Creative Brief
Professional
Owen Darlisk
2917 41st Lane Northeast Seattle WA 98422
owen@bramblepkit-example.com
www.bramblepkit-example.com
The original logo on the back, #34 and #35
Move Add and Changes, Corporate Relocation, Server Room Support, Technical Support

```html
<!DOCTYPE html>
<html lang="en">
<head>
<meta charset="utf-8">
<title>Bramble Peak Information Technology – Business Card</title>
<link rel="stylesheet" href="https://fonts.googleapis.com/css2?family=Montserrat:wght@400;500;700;800&display=swap">
<style>
  :root {
    --page-bg: #e9e7e4;
    --card-bg: #ffffff;
    --ink-dark: #2f2f2f;
    --ink-mid: #6b6b6b;
    --ink-soft: #9a9a9a;
    --accent: #f39a1e;
    --band-dark: #3b3b3d;
    --divider: #cfcfcf;
  }
  * { margin: 0; padding: 0; box-sizing: border-box; }
  html, body {
    width: 1200px; height: 901px; overflow: hidden;
    background: var(--page-bg);
    font-family: "Montserrat", sans-serif;
  }
  .card {
    position: absolute; left: 150px; top: 193px;
    width: 900px; height: 514px;
    background: var(--card-bg);
    border-radius: 34px;
    overflow: hidden;
    box-shadow: 0 18px 40px rgba(0,0,0,0.12);
  }
  .card-waves { position: absolute; inset: 0; width: 900px; height: 514px; }
  .brand {
    position: absolute; left: 78px; top: 196px;
    display: flex; align-items: center; gap: 12px;
  }
  .brand-dot {
    width: 22px; height: 22px; border-radius: 50%;
    background: var(--accent);
  }
  .brand-name {
    font-weight: 800; font-size: 34px; letter-spacing: 0.5px;
    color: var(--ink-dark); line-height: 1;
  }
  .divider {
    position: absolute; left: 440px; top: 44px;
    width: 1px; height: 236px; background: var(--divider);
  }
  .contact { position: absolute; left: 466px; top: 46px; }
  .contact-name {
    font-weight: 500; font-size: 24px; letter-spacing: 1px;
    color: var(--accent); text-transform: uppercase;
  }
  .contact-role { font-size: 15px; color: var(--ink-mid); margin-top: 4px; }
  .contact-address {
    font-size: 15px; color: var(--ink-mid); line-height: 1.4;
    margin-top: 22px; width: 300px;
  }
  .contact-lines { list-style: none; margin-top: 20px; }
  .contact-lines li {
    display: flex; align-items: center; gap: 12px;
    font-size: 14px; color: var(--ink-mid); height: 26px;
  }
  .contact-lines svg { width: 14px; height: 14px; fill: var(--accent); flex: none; }
</style>
</head>
<body>
  <div class="card">
    <svg class="card-waves" viewBox="0 0 900 514" aria-hidden="true">
      <path d="M0 514 L0 476 C 260 430 560 400 900 326 L900 514 Z" fill="var(--band-dark)"/>
      <path d="M0 446 C 290 392 600 362 900 288 L900 306 C 600 384 300 410 0 460 Z" fill="var(--accent)"/>
    </svg>

    <div class="brand">
      <span class="brand-dot"></span>
      <span class="brand-name">BRAMBLE PEAK</span>
    </div>

    <div class="divider"></div>

    <div class="contact">
      <p class="contact-name">Owen Darlisk</p>
      <p class="contact-role">Managing Director</p>
      <p class="contact-address">2917 41st Lane Northeast<br>Seattle WA 98422</p>
      <ul class="contact-lines">
        <li><svg viewBox="0 0 24 24"><path d="M6.6 10.8a15.2 15.2 0 0 0 6.6 6.6l2.2-2.2a1 1 0 0 1 1-.25 11.4 11.4 0 0 0 3.6.57 1 1 0 0 1 1 1V20a1 1 0 0 1-1 1A17 17 0 0 1 3 4a1 1 0 0 1 1-1h3.5a1 1 0 0 1 1 1c0 1.25.2 2.45.57 3.6a1 1 0 0 1-.25 1z"/></svg>012 345 6789</li>
        <li><svg viewBox="0 0 24 24"><rect x="3" y="3" width="18" height="18" rx="2"/></svg>012 345 6789</li>
        <li><svg viewBox="0 0 24 24"><rect x="6" y="2" width="12" height="20" rx="2"/></svg>012 345 6789</li>
        <li><svg viewBox="0 0 24 24"><path d="M2 5h20v14H2z M2 5l10 8 10-8" /></svg>owen@bramblepkit-example.com</li>
        <li><svg viewBox="0 0 24 24"><circle cx="12" cy="12" r="10"/></svg>www.bramblepkit-example.com</li>
      </ul>
    </div>
  </div>
</body>
</html>
```